Restaurant needs a vertical banner for fried catfish

Our restaurant is looking for an eye-catching 78.75in. x 36in. vertical physical banner ad for our fried catfish. Photos for the fried catfish will be provided as a reference but we will also accept anything similar to the photo. We will be using the following as our receptacle: https://www.plankoria.example/banner-stand/retractable-banner-stands/
The design must incorporate the following flavor texts:
Fried Catfish
Always Fresh!
Made from Scratch
Hand-cut Fillets
The Best Catfish in Texas
Served with fries, hush puppies, and a 32oz fountain drink
Also available by the pound!
The final design should be creative, professional, and eye-catching for customers.
Updates
Colors
Designer to choose colors to be used in the design.
Requirements
Must have
- We are open to any and all design elements, albeit the 'flavor texts' should not overpower, but complement the fried catfish photo. 'Fried Catfish' can be used in lieu of a main title/logo.
Nice to have
- Transparent or textured backgrounds that can encompass any or all part of the banner such as a cutting board, shadows, abstract, etc to show depth are a plus.
- Use of vectors or objects such as ribbons or shapes to encapsulate the 'flavor texts' are also encouraged.

```html
<!DOCTYPE html>
<html lang="en">
<head>
<meta charset="utf-8">
<title>Fried Catfish Banner</title>
<link rel="stylesheet" href="https://fonts.googleapis.com/css2?family=Holtwood+One+SC&family=Teko:wght@500;600&display=swap">
<style>
  :root {
    --bg: #e9e9ea;
    --paper: #fbfbfb;
    --ink: #262626;
    --brand-red: #990000;
    --gold: #f6b800;
    --white: #ffffff;
    --photo-deep: #8a3c12;
    --photo-mid: #c8741f;
    --photo-light: #e7b04a;
  }
  * { box-sizing: border-box; margin: 0; padding: 0; }
  html, body { width: 1200px; height: 1200px; overflow: hidden; background: var(--bg); }
  .banner {
    position: absolute; left: 339px; top: 30px;
    width: 522px; height: 1140px;
    background: var(--paper);
    overflow: hidden;
    box-shadow: 0 12px 30px rgba(0,0,0,0.18);
  }
  .banner-art { position: absolute; inset: 0; width: 522px; height: 1140px; }
  .title {
    position: absolute; left: 0; width: 100%; text-align: center;
    font-family: "Holtwood One SC", serif; color: var(--ink);
    line-height: 1;
  }
  .title-fried { top: 62px; font-size: 84px; letter-spacing: 2px; }
  .title-catfish { top: 154px; font-size: 60px; letter-spacing: 1px; }
  .tagline {
    position: absolute; left: 67px; top: 237px; width: 388px; height: 50px;
    background: var(--brand-red); color: var(--white);
    font-family: "Teko", sans-serif; font-weight: 600; font-size: 34px;
    display: flex; align-items: center; justify-content: center;
    padding-top: 6px; letter-spacing: 0.5px;
  }
  .features {
    position: absolute; left: 0; top: 782px; width: 100%;
    list-style: none; text-align: center;
    font-family: "Teko", sans-serif; font-weight: 600; color: var(--white);
    font-size: 48px; line-height: 54px; letter-spacing: 0.5px;
  }
  .features li::before {
    content: "»"; color: var(--gold); margin-right: 10px;
  }
  .served-box {
    position: absolute; left: 46px; top: 956px; width: 430px; height: 90px;
    background: var(--white); color: var(--ink);
    font-family: "Teko", sans-serif; font-weight: 600; font-size: 25px; line-height: 26px;
    display: flex; align-items: center; justify-content: center; text-align: center;
    padding-top: 6px;
  }
  .by-pound {
    position: absolute; left: 0; top: 1060px; width: 100%; text-align: center;
    font-family: "Teko", sans-serif; font-weight: 600; font-size: 28px; color: var(--gold);
    letter-spacing: 0.5px;
  }
</style>
</head>
<body>
  <div class="banner">
    <svg class="banner-art" viewBox="0 0 522 1140" xmlns="http://www.w3.org/2000/svg">
      <defs>
        <linearGradient id="platter" x1="0" y1="0" x2="1" y2="1">
          <stop offset="0" stop-color="#b8462a"/>
          <stop offset="0.35" stop-color="var(--photo-mid)"/>
          <stop offset="0.7" stop-color="var(--photo-deep)"/>
          <stop offset="1" stop-color="var(--photo-light)"/>
        </linearGradient>
        <linearGradient id="inset" x1="0" y1="0" x2="0" y2="1">
          <stop offset="0" stop-color="#c9502f"/>
          <stop offset="0.45" stop-color="#e9e2cf"/>
          <stop offset="1" stop-color="var(--photo-mid)"/>
        </linearGradient>
      </defs>
      <rect class="hero-photo" x="0" y="240" width="522" height="520" fill="url(#platter)" role="img" aria-label="Photo of golden fried catfish fillets on a plate with french fries, hush puppies and tomatoes"/>
      <path class="top-panel" d="M0,0 H522 V252 C420,330 200,360 0,300 Z" fill="var(--paper)"/>
      <path class="bottom-panel" d="M0,550 C60,680 200,745 330,745 C420,745 480,730 522,722 V1140 H0 Z" fill="var(--brand-red)"/>
      <circle class="inset-photo" cx="140" cy="665" r="102" fill="url(#inset)" stroke="var(--gold)" stroke-width="7" role="img" aria-label="Photo of a catfish plate with fillets, dipping sauce, tomatoes and lemons"/>
    </svg>

    <h1 class="title title-fried">FRIED</h1>
    <div class="title title-catfish">CATFISH</div>
    <div class="tagline">THE BEST CATFISH IN TEXAS</div>

    <ul class="features">
      <li>ALWAYS FRESH</li>
      <li>MADE FROM SCRATCH</li>
      <li>HANDCUT FILLETS</li>
    </ul>

    <div class="served-box">SERVED WITH FRIES HUSH PUPPIES AND<br>A 32OZ FOUNTAIN DRINK</div>
    <div class="by-pound">ALSO AVAILABLE BY THE POUND</div>
  </div>
</body>
</html>
```